Flyer-Design für Segelverein
Zielgruppe
Wir sind ein kleiner Berliner Segelverein im Herzen von Berlin. Unsere Zielgruppe sind wasserbegeisterte Menschen zwischen 20-50 Jahre.
Ein Eindruck über unseren Verein gibt es auf der neuen Webseite (noch im Aufbau): www.wellenrunde-kiel.de
und der alten webseite: www.wellenrundekiel.de
Aufgabenstellung
Wir benötigen den Flyer zum Anwerben neuer Mitglieder. D.h. der Flyer soll alle notwendigen Informationen beinhalten, auf das nötigste reduziert. Vom Format würden wir daher eher was kompaktes sehen (z.b. DIN lang beidseitig bedruckt). Dann könnte auf der Vorderseite die wichtigsten Informationen zum Verein stehen und auf der Rückseite Gründe, Mitglied zu werden.
Zum Verein
1972 gegründet mit dem Ziel, das Seesegeln zu fördern. Die damalige Begeisterung, gemeinsam etwas vollbringen zu können, führte in den Jahren 1975/76 zu einer Folge von Seetörns, bei der ausnahmslos Mitglieder beteiligt waren, von der Ostsee über Norwegen, England, Kanarische Inseln, Karibik über die Bermudas und Azoren wieder zurück in die Ostsee.
Warum der Verein:
- Verkehrsgünstig und zentral gelegen direkt an der Lindgasse - Sehr gut zu erreichen mit den ÖPNVs
- Einzigartiger Schwimmsteg in Berlin ohne Landzugang - Ein Ort zum Verweilen und Abschalten
- verfügbare Stegplätze für Bootsbesitzer
- Viele Vereinsboote für Mitglieder ohne Boot -
- Günstige Mitgliedsbeiträge - Studenten und Schüler erhalten Ermässigungen
- Ein familiärer kleiner Verein - Keine umfangreichen Pflichtarbeiten
- Vereinsinterne Regatten entlang der Havel
- Spannende interne Events und Ausbildungsangebote wie z.b. Fahrten mit dem Dreimast-Gaffelschooner Solvenja, Knotenkurse, Navigation

```html
<!DOCTYPE html>
<html lang="de">
<head>
<meta charset="utf-8">
<title>Wellenrunde Kiel – Flyer</title>
<link href="https://fonts.googleapis.com/css2?family=Cabin:wght@400;500;600&display=swap" rel="stylesheet">
<style>
  :root {
    --slate: #4b505d;
    --slate-dark: #2f333c;
    --coral: #d2665a;
    --paper: #f3f2ef;
    --ink: #3a3e48;
    --backdrop: #5a5a5a;
    --sky-top: #b9c3db;
    --sky-bottom: #d8dcea;
    --water: #7d93ad;
  }
  * { box-sizing: border-box; margin: 0; padding: 0; }
  html, body { width: 800px; height: 1200px; overflow: hidden; }
  body {
    background: var(--backdrop);
    font-family: "Cabin", sans-serif;
    display: flex;
    align-items: center;
    justify-content: center;
    gap: 20px;
  }
  .page {
    position: relative;
    width: 370px;
    height: 530px;
    overflow: hidden;
    box-shadow: 0 6px 18px rgba(0,0,0,.35);
  }

  /* Front */
  .front { background: var(--slate); }
  .front-header { height: 82px; padding: 12px 14px; color: #fff; }
  .front-header .greeting { font-size: 19px; }
  .brand { display: flex; align-items: center; gap: 14px; margin-top: 4px; }
  .brand-dot { width: 16px; height: 16px; border-radius: 50%; background: var(--coral); flex: none; }
  .brand-name { font-size: 27px; font-weight: 500; }
  .front .stripe { height: 12px; background: var(--coral); }
  .harbour-photo {
    height: 246px;
    background: linear-gradient(180deg, var(--sky-top) 0%, var(--sky-bottom) 62%, var(--water) 63%, var(--water) 100%);
  }
  .front .divider { height: 22px; background: var(--slate); }
  .front-cta {
    position: absolute; left: 0; right: 0; bottom: 0; height: 168px;
    background: var(--coral); color: #fff; padding: 12px 14px 16px;
    display: flex; flex-direction: column; justify-content: space-between;
  }
  .front-cta .lead { font-size: 19px; line-height: 1.15; }
  .front-cta .headline { font-size: 52px; font-weight: 500; line-height: 1; }
  .about-box {
    position: absolute; right: 20px; top: 238px; width: 150px; height: 178px;
    background: var(--paper); color: var(--ink);
    font-size: 8px; line-height: 1.25; text-align: justify; padding: 9px 10px;
    hyphens: auto;
  }

  /* Back */
  .back { background: var(--slate-dark); }
  .back-photo {
    position: absolute; inset: 0;
    background: linear-gradient(160deg, #3e434d 0%, #5f6673 45%, #8a919c 70%, #4a4f59 100%);
  }
  .back-content { position: relative; }
  .back-title { color: #fff; font-size: 30px; font-weight: 500; padding: 18px 14px 14px; background: rgba(47,51,60,.8); }
  .back .stripe { height: 12px; background: var(--coral); }
  .reasons { list-style: none; padding: 16px 0 0 0; }
  .reasons li {
    background: rgba(243,242,239,.88); color: var(--ink);
    font-size: 15px; margin: 0 12px 8px 12px; padding: 6px 8px;
  }
  .contact {
    position: absolute; left: 0; right: 0; bottom: 0; height: 98px;
    background: var(--coral); color: #fff; padding: 8px 12px;
  }
  .contact h2 { font-size: 17px; font-weight: 500; margin-bottom: 6px; }
  .contact-grid { display: grid; grid-template-columns: 1fr 1fr; gap: 6px 10px; font-size: 10.5px; }
  .contact-item { display: flex; align-items: center; gap: 6px; }
  .contact-item svg { width: 14px; height: 14px; flex: none; }
</style>
</head>
<body>

  <section class="page front">
    <header class="front-header">
      <p class="greeting">Willkommen bei der</p>
      <div class="brand"><span class="brand-dot"></span><span class="brand-name">Wellenrunde Kiel</span></div>
    </header>
    <div class="stripe"></div>
    <div class="harbour-photo" role="img" aria-label="Foto: Segelboote mit Masten im Hafen unter blauem Himmel"></div>
    <div class="divider"></div>
    <div class="front-cta">
      <p class="lead">Werde Mitglied &amp;<br>sei Teil einer starken</p>
      <p class="headline">Mannschaft!</p>
    </div>
    <p class="about-box">Der Verein wurde 1972 mit dem Ziel gegründet, dass Seesegeln zu fördern. Die damalige Begeisterung, gemeinsam etwas vollbringen zu können, führte 1975/1976 zu einer Folge von Seetörns, bei der ausnahmslos Mitglieder von der Ostsee über Norwegen, Kanarische Inseln, Karibik über die Bermudas und Azoren wieder zurück in die Ostsee, beteiligt waren.</p>
  </section>

  <section class="page back">
    <div class="back-photo" role="img" aria-label="Gedämpftes Hintergrundfoto: Segelboot am Steg"></div>
    <div class="back-content">
      <h1 class="back-title">Warum der Verein?</h1>
      <div class="stripe"></div>
      <ul class="reasons">
        <li>- Zentrale Lage (gut zu erreichen, ÖPNV)</li>
        <li>- Einzigartiger Schwimmsteg in Berlin</li>
        <li>- Verfügbare Stegplätze für Bootsbesitzer</li>
        <li>- Viele Vereinsboote für Mitglieder</li>
        <li>- Günstige Mitgliedsbeiträge</li>
        <li>- Keine umfangreichen Pflichtarbeiten</li>
        <li>- Vereinsinterne Regatten entlang der Havel</li>
        <li>- Interne Events &amp; Ausbildungsmöglichkeiten</li>
      </ul>
    </div>
    <footer class="contact">
      <h2>Kontakt</h2>
      <div class="contact-grid">
        <div class="contact-item">
          <svg viewBox="0 0 24 24"><path d="M12 2a7 7 0 0 0-7 7c0 5 7 13 7 13s7-8 7-13a7 7 0 0 0-7-7zm0 9.5A2.5 2.5 0 1 1 12 6.5a2.5 2.5 0 0 1 0 5z" fill="#fff"/></svg>
          <span>Am Uferweg 12, 10115 Berlin</span>
        </div>
        <div class="contact-item">
          <svg viewBox="0 0 24 24"><rect x="2" y="5" width="20" height="14" rx="1" fill="none" stroke="#fff" stroke-width="2"/><path d="M2 6l10 7 10-7" fill="none" stroke="#fff" stroke-width="2"/></svg>
          <span>info@wellenrunde-kiel.de</span>
        </div>
        <div class="contact-item">
          <svg viewBox="0 0 24 24"><path d="M6.6 10.8a15 15 0 0 0 6.6 6.6l2.2-2.2a1 1 0 0 1 1-.25 11.4 11.4 0 0 0 3.6.57 1 1 0 0 1 1 1V20a1 1 0 0 1-1 1A17 17 0 0 1 3 4a1 1 0 0 1 1-1h3.5a1 1 0 0 1 1 1c0 1.25.2 2.450.57 3.57a1 1 0 0 1-.25 1z" fill="#fff"/></svg>
          <span>+49 (030) 555 01 23</span>
        </div>
        <div class="contact-item">
          <svg viewBox="0 0 24 24"><circle cx="12" cy="12" r="9" fill="none" stroke="#fff" stroke-width="2"/><path d="M3 12h18M12 3c3 3 3 15 0 18M12 3c-3 3-3 15 0 18" fill="none" stroke="#fff" stroke-width="1.5"/></svg>
          <span>www.wellenrunde-kiel.de</span>
        </div>
      </div>
    </footer>
  </section>

</body>
</html>
```